Business Card Design and Stationary design for consulting firm

Harbourline Sourcing are looking for a new business card design and a design for their A4 letterhead / A4 invoices.

We are seeking to heavily increase our brand awareness and require a business card that's professional in appearance but also shows flare and innovation. A card design that people will remember.

About Us
Harbourline Sourcing are `The Sourcing Crew’.
Our mission is to be one of Australia’s greatest companies. Our aim is to help our customers achieve the best result from their purchasing experience.

Our Requirement:
• IMPACT! IMPACT! IMPACT!
• BUSINESS & PROFESSIONAL LOOKING

• Our business colours are orange, blue and green (See the logo attached).

We have provided an Art Design specification (attached) that needs to be followed for you to win the design. This also has the font, which is used on the logo.

We are after a two sided business card

Side One should have the:
The company Logo
The Sourcing Crew
www.harbourlinesourcing.com.au
Procure | Personnel | Probity & Privacy
Sydney | Melbourne | Adelaide | Brisbane

Side Two
Logo (optional)
Harbourline Sourcing (optional)
Employee details (details listed below)

The above format is our preferred option, but if you think you can come up with something better, feel free to put it forward.

We are leaving the design up to you, but it must incorporate the logo.

We will need a template that we can change the employee details on, as we will be adding more staff over the coming months.

The details below are for one employee per card with the same design.
------------------------

Employee Details:

Marcus Del Arroyo MBA, MMgmtStratProc
Principal Consultant
0491 372 618
Marcus@harbourlinesourcing.com.au

Brianna Tolley
Consulting Manager
0462 915 308
Brianna@harbourlinesourcing.com.au

Our website is www.harbourlinesourcing.com.au

The Letterhead / invoice needs to incorporate:
the company Logo
The Sourcing Crew
Sydney | Melbourne | Adelaide | Brisbane but otherwise the design is over to you.

This file needs to be delivered in word format as other detail will be added to the documents.

We look forward to you award winning designs. If you require any further information please feel free to contact us.

Regards
Harbourline Sourcing

Target Market(s)

Our Target market is companies with 80+ employees. The market we segment is heavily male based, between the ages of 35-55 years of age.

Industry/Entity Type

Consulting

Contact Information for Business Card

See Project Description

Font styles to use
Other font styles liked:
• See Art Specification

Requirements
Must have
• Company Colours, See Project Description
Should not have
• Be outside the Art specification guidelines

```html
<!DOCTYPE html>
<html lang="en">
<head>
<meta charset="utf-8">
<title>Harbourline Sourcing – Business Card</title>
<link rel="stylesheet" href="https://fonts.googleapis.com/css2?family=Josefin+Sans:wght@400;600&family=Share+Tech+Mono&display=swap">
<style>
  :root {
    --page: #e9e7e3;
    --card-white: #ffffff;
    --ink-dark: #3d3f42;
    --ink-mid: #55585c;
    --brand-blue: #1d73c2;
    --brand-blue-light: #2a9be0;
    --brand-orange: #f15a24;
    --brand-orange-light: #f7a13a;
    --brand-green-light: #8cc63f;
    --brand-green-dark: #17994a;
    --on-green: #ffffff;
  }
  * { box-sizing: border-box; margin: 0; padding: 0; }
  html, body { width: 960px; height: 1200px; overflow: hidden; }
  body {
    background: var(--page);
    font-family: "Josefin Sans", sans-serif;
    display: flex;
    flex-direction: column;
    align-items: center;
    justify-content: center;
    gap: 56px;
  }
  .card {
    position: relative;
    width: 800px;
    height: 518px;
    overflow: hidden;
    box-shadow: 0 6px 18px rgba(0,0,0,0.12);
  }

  /* Front */
  .card-front { background: var(--card-white); }
  .front-brand {
    position: absolute;
    left: 30px;
    top: 190px;
    width: 262px;
    text-align: center;
  }
  .brand-dot {
    display: block;
    width: 46px;
    height: 46px;
    border-radius: 50%;
    margin: 0 auto 18px;
  }
  .front-brand .brand-dot { background: var(--brand-blue-light); }
  .front-brand .brand-name {
    font-weight: 600;
    font-size: 25px;
    letter-spacing: 1px;
    color: var(--ink-dark);
    line-height: 1.1;
  }
  .employee {
    position: absolute;
    left: 402px;
    top: 160px;
  }
  .employee-name {
    font-weight: 400;
    font-variant: small-caps;
    font-size: 30px;
    letter-spacing: 1px;
    color: var(--brand-blue);
    line-height: 1;
  }
  .employee-credentials {
    font-variant: small-caps;
    font-weight: 600;
    font-size: 15px;
    color: var(--ink-dark);
    margin-top: 2px;
    margin-left: 3px;
  }
  .employee-title {
    font-family: "Share Tech Mono", monospace;
    font-size: 11px;
    letter-spacing: 3px;
    text-transform: uppercase;
    color: var(--ink-mid);
    margin-top: 4px;
    margin-left: 3px;
  }
  .contact {
    position: absolute;
    left: 402px;
    top: 310px;
    font-family: "Share Tech Mono", monospace;
    font-size: 15px;
    letter-spacing: 2px;
    color: var(--ink-dark);
    line-height: 22px;
  }
  .contact-email { text-transform: uppercase; font-size: 13px; }
  .front-bands {
    position: absolute;
    left: 0;
    bottom: 0;
    width: 800px;
    height: 26px;
  }

  /* Back */
  .card-back {
    background: linear-gradient(90deg, var(--brand-green-light) 0%, var(--brand-green-dark) 100%);
    color: var(--on-green);
    text-align: center;
  }
  .back-brand {
    position: absolute;
    left: 0;
    right: 0;
    top: 168px;
  }
  .back-brand .brand-dot { background: var(--on-green); width: 52px; height: 52px; }
  .back-brand .brand-name {
    font-weight: 600;
    font-size: 30px;
    letter-spacing: 1.5px;
    line-height: 1.1;
  }
  .back-details {
    margin-top: 20px;
    font-variant: small-caps;
    font-size: 16px;
    letter-spacing: 1px;
    line-height: 16px;
  }
  .back-details .url { text-transform: uppercase; font-size: 13px; }
</style>
</head>
<body>

  <section class="card card-front" aria-label="Business card front">
    <div class="front-brand">
      <span class="brand-dot"></span>
      <div class="brand-name">Harbourline Sourcing</div>
    </div>

    <div class="employee">
      <h1 class="employee-name">Marcus Del Arroyo</h1>
      <p class="employee-credentials">MBA, MMgmtStratProc</p>
      <p class="employee-title">Principal Consultant</p>
    </div>

    <div class="contact">
      <p class="contact-phone">0491 372 618</p>
      <p class="contact-email">Marcus@harbourlinesourcing.com.au</p>
    </div>

    <svg class="front-bands" viewBox="0 0 800 26" aria-hidden="true">
      <defs>
        <linearGradient id="band-blue" x1="0" x2="1">
          <stop offset="0" stop-color="#2a9be0"/>
          <stop offset="1" stop-color="#1d63b0"/>
        </linearGradient>
        <linearGradient id="band-orange" x1="0" x2="1">
          <stop offset="0" stop-color="#f7a13a"/>
          <stop offset="1" stop-color="#f15a24"/>
        </linearGradient>
      </defs>
      <polygon points="0,0 398,0 388,26 0,26" fill="url(#band-blue)"/>
      <polygon points="406,0 800,0 800,26 396,26" fill="url(#band-orange)"/>
    </svg>
  </section>

  <section class="card card-back" aria-label="Business card back">
    <div class="back-brand">
      <span class="brand-dot"></span>
      <div class="brand-name">Harbourline Sourcing</div>
      <div class="back-details">
        <p class="tagline">The Sourcing Crew</p>
        <p class="url">www.harbourlinesourcing.com.au</p>
        <p class="services">Procure | Personnel | Probity &amp; Privacy</p>
        <p class="cities">Sydney | Melbourne | Adelaide | Brisbane</p>
      </div>
    </div>
  </section>

</body>
</html>
```